Business Card for Industrial Distributor

We need a business card design for an industrial distributor. We sell machine parts for the manufacturing and oil industry. We would like the cards to look clean and modern but with a touch of industry.

Our colors are blue/white.

Please feel free to visit our website www.krovelmint.com

Target Market(s)

mexican manufacturers in the automobile/aerospace industry

Industry/Entity Type

Industrial

Colors
ffffff
0555a3

```html
<!DOCTYPE html>
<html lang="en">
<head>
<meta charset="utf-8">
<title>Krovelmint Business Card</title>
<link rel="stylesheet" href="https://fonts.googleapis.com/css2?family=Arimo:wght@400;700&display=swap">
<style>
  :root {
    --brand-blue: #0555a3;
    --deep-blue: #25349a;
    --light-blue: #0a72c8;
    --band-grey: #a9abb0;
    --paper: #ffffff;
    --stage: #e6e8eb;
  }
  * { margin: 0; padding: 0; box-sizing: border-box; }
  html, body { width: 1200px; height: 800px; overflow: hidden; }
  body {
    background: var(--stage);
    font-family: "Arimo", Arial, sans-serif;
    position: relative;
  }
  .card {
    position: absolute;
    top: 250px;
    width: 525px;
    height: 300px;
    overflow: hidden;
    box-shadow: 0 6px 18px rgba(0,0,0,0.15);
  }
  /* Back side */
  .card-back {
    left: 45px;
    background: radial-gradient(ellipse at 50% 45%, var(--light-blue) 0%, var(--brand-blue) 45%, var(--deep-blue) 100%);
    display: flex;
    align-items: center;
    justify-content: center;
  }
  .card-back .wordmark {
    color: var(--paper);
    font-weight: 700;
    font-size: 64px;
    letter-spacing: -1px;
  }
  /* Front side */
  .card-front {
    left: 630px;
    background: var(--paper);
  }
  .front-logo {
    position: absolute;
    top: 38px;
    left: 0;
    width: 100%;
    display: flex;
    align-items: center;
    justify-content: center;
    gap: 14px;
  }
  .front-logo .dot {
    width: 52px;
    height: 52px;
    border-radius: 50%;
    background: var(--brand-blue);
  }
  .front-logo .wordmark {
    color: var(--deep-blue);
    font-weight: 700;
    font-size: 50px;
    letter-spacing: -1px;
  }
  .name-rule {
    position: absolute;
    top: 112px;
    left: 24px;
    right: 24px;
    display: flex;
    align-items: center;
    gap: 12px;
  }
  .name-rule .line {
    flex: 1;
    height: 1px;
    background: var(--brand-blue);
  }
  .name-rule .person {
    color: var(--deep-blue);
    font-weight: 700;
    font-size: 15px;
    letter-spacing: 0.5px;
  }
  .contact-band {
    position: absolute;
    top: 138px;
    left: 0;
    right: 0;
    height: 28px;
    background: var(--band-grey);
    display: flex;
    align-items: center;
    justify-content: space-around;
    padding: 0 14px;
  }
  .contact-item {
    display: flex;
    align-items: center;
    gap: 6px;
    color: var(--paper);
    font-size: 12px;
  }
  .contact-item .icon {
    width: 16px;
    height: 16px;
    background: var(--deep-blue);
    display: flex;
    align-items: center;
    justify-content: center;
  }
  .info-panel {
    position: absolute;
    top: 166px;
    left: 0;
    right: 0;
    bottom: 0;
    background: var(--deep-blue);
    color: var(--paper);
    text-align: center;
    padding-top: 34px;
    line-height: 1.45;
  }
  .info-panel .company { font-weight: 700; font-size: 15px; }
  .info-panel .address, .info-panel .web { font-size: 13px; }
</style>
</head>
<body>
  <div class="card card-back">
    <span class="wordmark">Krovelmint</span>
  </div>

  <div class="card card-front">
    <div class="front-logo">
      <span class="dot"></span>
      <span class="wordmark">Krovelmint</span>
    </div>

    <div class="name-rule">
      <span class="line"></span>
      <span class="person">DANIEL ROURKE</span>
      <span class="line"></span>
    </div>

    <div class="contact-band">
      <div class="contact-item">
        <span class="icon">
          <svg width="10" height="10" viewBox="0 0 10 10"><path d="M2 1 L4 1 L4.6 3 L3.4 3.8 Q4.4 5.8 6.2 6.6 L7 5.4 L9 6 L9 8 Q8.6 9 7.6 9 Q1 8.4 1 2.4 Q1 1.4 2 1 Z" fill="#fff"/></svg>
        </span>
        <span>(555) 014 - 2280</span>
      </div>
      <div class="contact-item">
        <span class="icon">
          <svg width="10" height="10" viewBox="0 0 10 10"><rect x="1" y="4" width="8" height="5" fill="#fff"/><rect x="2.5" y="1" width="5" height="3" fill="none" stroke="#fff" stroke-width="1"/></svg>
        </span>
        <span>(555) 014 - 2291</span>
      </div>
      <div class="contact-item">
        <span class="icon">
          <svg width="10" height="10" viewBox="0 0 10 10"><rect x="1" y="2.5" width="8" height="5.5" fill="#fff"/><path d="M1 2.5 L5 6 L9 2.5" fill="none" stroke="#25349a" stroke-width="0.8"/></svg>
        </span>
        <span>sales@krovelmint.com</span>
      </div>
    </div>

    <div class="info-panel">
      <div class="company">Krovelmint International Corp.</div>
      <div class="address">4120 Harlow Ridge Rd. Calder, TX 70412</div>
      <div class="web">www.krovelmint.com</div>
    </div>
  </div>
</body>
</html>
```